Webseite Toilettenvermietung
Zielgruppe
Wir vermieten mobile Toilettenkabine und Toilettenwagen. Wir haben noch eine Webseite kabinenpark-nord.de und lokus-verleihhaus.de und benötigen noch eine weitere. Es sollen nur die Miettoiletten und Toilettenwagen beworben werden
Aufgabenstellung
saubere und aussageräftige, farbliches Erscheinungsbild der Startseite.

```html
<!DOCTYPE html>
<html lang="de">
<head>
<meta charset="utf-8">
<title>Klarwerk – Mobile WC Kabinen mieten</title>
<link href="https://fonts.googleapis.com/css2?family=Roboto:wght@300;400;500&display=swap" rel="stylesheet">
<style>
:root{
  --page-bg:#f0f0f0;
  --white:#ffffff;
  --blue:#1565b8;
  --blue-dark:#0f55a3;
  --blue-hero-a:#1a64b4;
  --blue-hero-b:#2a7fd0;
  --cyan:#1fa6de;
  --green:#8cc21e;
  --text-dark:#333333;
  --text-grey:#8a8a8a;
  --text-mid:#777777;
  --line:#e2e2e2;
  --soft:#f7f7f7;
}
*{margin:0;padding:0;box-sizing:border-box}
html,body{width:1200px;height:1012px;overflow:hidden}
body{background:var(--page-bg);font-family:'Roboto',sans-serif;font-weight:300;position:relative;color:var(--text-grey)}
.site-header{position:absolute;left:0;top:0;width:1200px;height:44px;background:var(--white);border-bottom:1px solid #d6d6d6}
.brand{position:absolute;left:300px;top:9px;display:flex;align-items:center;gap:6px;color:var(--blue);font-weight:500;font-size:16px}
.brand-dot{width:20px;height:20px;border-radius:50%;background:var(--blue)}
.main-nav{position:absolute;top:15px;font-size:10px;font-weight:300;color:var(--text-grey)}
.main-nav a{position:absolute;white-space:nowrap;color:inherit;text-decoration:none}
.main-nav a.active{color:var(--blue)}
.page{position:absolute;left:300px;top:44px;width:600px;height:945px;background:var(--white)}
.hero{position:absolute;left:0;top:0;width:600px;height:281px;box-shadow:0 10px 10px -6px rgba(0,0,0,.35)}
.hero-panel{position:absolute;left:0;top:0;width:300px;height:281px;background:linear-gradient(135deg,var(--blue-hero-a),var(--blue-hero-b));color:var(--white)}
.hero-title{position:absolute;left:20px;top:38px;font-size:19px;font-weight:300;letter-spacing:.2px;white-space:nowrap}
.hero-sub{position:absolute;left:20px;top:67px;font-size:15px;color:var(--cyan);font-weight:300}
.hero-text{position:absolute;left:18px;top:104px;width:270px;font-size:8.3px;line-height:10.4px;font-weight:300}
.hero-text p+p{margin-top:10.4px}
.btn{position:absolute;background:var(--green);color:var(--white);text-align:center;font-weight:300}
.hero-btn{left:17px;top:217px;width:87px;height:21px;line-height:21px;font-size:11px}
.hero-visual{position:absolute;left:300px;top:0;width:300px;height:281px;background:linear-gradient(160deg,#ffffff,#ececec)}
.hero-product{position:absolute;left:80px;top:20px;width:142px;height:242px;border-radius:10px 10px 4px 4px;background:linear-gradient(90deg,#15b9a6,#2dd3bd 55%,#1aa795)}
.slider-dots{position:absolute;left:273px;top:272px;width:54px;height:18px;background:var(--white);border:1px solid #ddd;border-radius:3px;display:flex;justify-content:center;align-items:center;gap:5px}
.slider-dots span{width:7px;height:7px;border-radius:50%;border:1px solid #999}
.slider-dots span.on{background:var(--blue);border-color:var(--blue)}
.services{position:absolute;left:0;top:312px;width:600px}
.service{position:absolute;top:0;width:156px;height:194px;border:1px solid var(--line);border-top:2px solid var(--blue-dark);text-align:center;background:var(--white)}
.service-icon{position:absolute;left:48px;top:17px;width:60px;height:60px}
.service h3{position:absolute;left:0;right:0;top:93px;font-size:13.5px;font-weight:400;color:var(--text-dark)}
.service p{position:absolute;left:16px;right:16px;top:114px;font-size:8.8px;line-height:15px}
.service a{position:absolute;left:0;right:0;top:165px;font-size:9px;font-weight:400;color:var(--blue);text-decoration:none}
.info{position:absolute;left:0;top:537px;width:600px;height:214px;background:var(--soft);border-top:1px solid var(--line);border-bottom:1px solid var(--line)}
.info h2{position:absolute;top:13px;font-size:19px;font-weight:300;color:var(--text-dark)}
.info p{position:absolute;top:47px;font-size:8.5px;line-height:13.75px;white-space:nowrap}
.about h2,.about p{left:37px}
.news h2,.news p{left:406px}
.info-divider{position:absolute;left:383px;top:22px;width:1px;height:169px;background:#dcdcdc}
.news-btn{left:472px;top:174px;width:88px;height:22px;line-height:22px;font-size:8.5px}
.products h2{position:absolute;left:0;width:600px;top:769px;text-align:center;font-size:15px;font-weight:300;color:var(--blue)}
.product{position:absolute;top:803px;text-align:center}
.product-shot{margin:0 auto;height:87px}
.product-name{margin-top:15px;font-size:10px;line-height:12px;color:var(--text-grey);white-space:nowrap}
.product-name.active{color:var(--blue)}
.site-footer{position:absolute;left:305px;top:996px;font-size:8.5px;font-weight:400;color:var(--text-mid);display:flex;gap:9px}
</style>
</head>
<body>
<header class="site-header">
  <div class="brand"><span class="brand-dot"></span>Klarwerk</div>
  <nav class="main-nav">
    <a class="active" style="left:626px">Startseite</a>
    <a style="left:693px">Miettoiletten</a>
    <a style="left:772px">Toilettenwagen</a>
    <a style="left:864px">Kontakt</a>
  </nav>
</header>

<main class="page">
  <section class="hero">
    <div class="hero-panel">
      <h1 class="hero-title">MOBILE WC KABINEN MIETEN</h1>
      <div class="hero-sub">BAUSTELLEN WC</div>
      <div class="hero-text">
        <p>Nicht auf jeder Großbaustelle finden sich für die Arbeiter Sanitärein­richtungen. Praktisch und gleichzeitig funktional sind Baustellen WC's der Firma Klarwerk, mit denen alle Anforderungen für das Per­sonal erfüllt sind.</p>
        <p>Die Ausstattung der Baustellen WC's besteht neben einem licht­durchlässigen Dach aus einer doppelwandigen Türfront mit Verriege­lungsmöglichkeit, die durch einen vorhandenen Türgriff schnell geöffnet und geschlossen werden kann.</p>
      </div>
      <div class="btn hero-btn">DETAILS</div>
    </div>
    <div class="hero-visual">
      <div class="hero-product" role="img" aria-label="Türkisfarbene mobile WC-Kabine"></div>
    </div>
    <div class="slider-dots"><span class="on"></span><span></span><span></span></div>
  </section>

  <section class="services">
    <article class="service" style="left:37px">
      <svg class="service-icon" viewBox="0 0 60 60"><circle cx="30" cy="30" r="30" fill="#1565b8"/><g stroke="#fff" stroke-width="2.2" fill="none" stroke-linecap="round"><line x1="43" y1="15" x2="33" y2="26"/><path d="M33 26 L22 30 L19 40 L28 38 Z"/><line x1="23" y1="34" x2="27" y2="31"/></g><circle cx="33" cy="40" r="1.4" fill="#fff"/><circle cx="38" cy="43" r="1.4" fill="#fff"/></svg>
      <h3>Clean</h3>
      <p>Lorem Ipsum is simply dummy text of the printing and typesetting industry.</p>
      <a>Read More</a>
    </article>
    <article class="service" style="left:222px">
      <svg class="service-icon" viewBox="0 0 60 60"><circle cx="30" cy="30" r="29" fill="#fff" stroke="#1565b8" stroke-width="1.2"/><rect x="13" y="19" width="21" height="17" rx="1" fill="#1565b8"/><path d="M35 24 h7 l5 6 v6 h-12 z" fill="#1565b8"/><rect x="38" y="26" width="4" height="4" fill="#fff"/><circle cx="20" cy="38" r="3.5" fill="#1565b8" stroke="#fff" stroke-width="1.5"/><circle cx="41" cy="38" r="3.5" fill="#1565b8" stroke="#fff" stroke-width="1.5"/></svg>
      <h3>Transport</h3>
      <p>Lorem Ipsum is simply dummy text of the printing and typesetting industry.</p>
      <a>Read More</a>
    </article>
    <article class="service" style="left:406px">
      <svg class="service-icon" viewBox="0 0 60 60"><circle cx="30" cy="30" r="29" fill="#fff" stroke="#1565b8" stroke-width="1.2"/><g stroke="#1565b8" stroke-linecap="round"><line x1="19" y1="19" x2="41" y2="41" stroke-width="4"/><line x1="41" y1="19" x2="20" y2="40" stroke-width="4"/></g><circle cx="42" cy="18" r="5" fill="#fff" stroke="#1565b8" stroke-width="3"/><rect x="14" y="15" width="6" height="4" fill="#1565b8" transform="rotate(45 17 17)"/></svg>
      <h3>Installation</h3>
      <p>Lorem Ipsum is simply dummy text of the printing and typesetting industry.</p>
      <a>Read More</a>
    </article>
  </section>

  <section class="info">
    <div class="about">
      <h2>About Klarwerk</h2>
      <p>Lorem Ipsum is simply dummy text of the printing and typesetting industry.<br>Lorem Ipsum has been the industry's standard dummy text ever since the 1500s,<br>when an unknown printer took a galley of type and scrambled it to make a type<br>specimen book.<br>It has survived not only five centuries, but also the leap into electronic typesetting,<br>remaining essentially unchanged.<br>It was popularised in the 1960s with the release of Setzbogen sheets containing<br>Lorem Ipsum passages, and more recently with desktop publishing software like<br>Satzwerk Pro including versions of Lorem Ipsum.</p>
    </div>
    <div class="info-divider"></div>
    <div class="news">
      <h2>News</h2>
      <p>Lorem Ipsum is simply dummy text of<br>the printing and typesetting industry.<br>Lorem Ipsum has been the industry's<br>standard dummy text ever since the<br>1500s, when an unknown printer took a<br>galley of type and scrambled it to make<br>a type specimen book. It has survived<br>not only five centuries.</p>
      <div class="btn news-btn">More News</div>
    </div>
  </section>

  <section class="products">
    <h2>Products</h2>
    <div class="product" style="left:36px;width:100px">
      <div class="product-shot" role="img" aria-label="Blaue mobile WC-Kabine" style="width:46px;border-radius:8px 8px 2px 2px;background:linear-gradient(90deg,#1a6fd0,#3d94ea,#1a64be)"></div>
      <div class="product-name active">MOBILE WC KABINEN<br>MIETEN</div>
    </div>
    <div class="product" style="left:166px;width:110px">
      <div class="product-shot" role="img" aria-label="Sanitärcontainer mit mehreren Türen" style="width:110px;height:78px;margin-top:6px;background:linear-gradient(90deg,#bfc3c8 45%,#f2f2f2 45%);border:4px solid #2c3580"></div>
      <div class="product-name" style="margin-top:18px">MOBILE WC CONTAINER<br>MIETEN</div>
    </div>
    <div class="product" style="left:300px;width:100px">
      <div class="product-shot" role="img" aria-label="Graue mobile WC-Anlage" style="width:50px;border-radius:8px 8px 2px 2px;background:linear-gradient(90deg,#7f8589,#a9aeb2,#6f7478)"></div>
      <div class="product-name">MOBILE WC ANLAGEN<br>KAUFEN</div>
    </div>
    <div class="product" style="left:418px;width:140px">
      <div class="product-shot" role="img" aria-label="Weißer Toilettenwagen mit zwei Eingängen" style="width:140px;height:72px;margin-top:10px;background:linear-gradient(180deg,#f4f6f8 80%,#2c3580 80%)"></div>
      <div class="product-name" style="margin-top:20px">MOBILE WC WAGEN<br>MIETEN</div>
    </div>
  </section>
</main>

<footer class="site-footer">
  <span>Produkte</span><span>News &amp; Infos</span><span>Unternehmen</span><span>Kontakt</span><span>AGB</span><span>Impressum</span>
</footer>
</body>
</html>
```